Primary Home Page Graphic: Crowdfund and Non-Profit Social Promotion Website

WHAT WE NEED: See attached. I need a graphic designed that is comparable to these. The graphic will replace the home page video on our current website Quenvale.com
PREFERRED LOOK: Much like attached. Black/white with color that pops. Must have crowdfunding/non-profit + social media appearance.
WHAT WE DO: Social Promotion of Crowdfunding and Non-Profit Campaigns > the image you design should reflect this subject content.
TEXT ON GRAPHIC:
Your Campaign, Shared.
Get your message moving across social media within minutes.
Thousands of social voices are on stand-by and ready to assist.
Project Deadline Extended
Reason: Not seeing the perfect fit yet for the page. Want to see if we can get some other ideas. Looking for black and white image with title and text displayed in a modern way.
The main graphic needs to appear such as Crowdfunding. Keep the text the same with a call to action.
Please use close attention to detail, modern design technique and good contrast on the colors. Thanks.
Non Profit

```html
<!DOCTYPE html>
<html lang="en">
<head>
<meta charset="utf-8">
<title>Quenvale — Your Campaign, Shared</title>
<link rel="stylesheet" href="https://fonts.googleapis.com/css2?family=Open+Sans:wght@300;400;600;700;800&display=swap">
<style>
  :root {
    --hero-bg: #5c5d62;
    --hero-deep: #54565d;
    --white: #ffffff;
    --ink: #2b2f36;
    --text: #1e1e1e;
    --rule: #e3e3e3;
    --accent: #f26b1d;
    --step-ring: #444444;
  }
  * { box-sizing: border-box; margin: 0; padding: 0; }
  html, body { width: 1200px; height: 899px; overflow: hidden; }
  body { font-family: "Open Sans", Arial, sans-serif; background: var(--white); position: relative; }

  .hero { position: absolute; left: 0; top: 0; width: 1200px; height: 766px; overflow: hidden; }
  .hero-backdrop { position: absolute; inset: 0; background: radial-gradient(ellipse at 35% 40%, var(--hero-bg) 0%, var(--hero-deep) 70%, #505259 100%); }

  .main-nav { position: absolute; top: 55px; left: 0; width: 1200px; }
  .main-nav a { position: absolute; color: var(--white); font-size: 11px; font-weight: 700; text-decoration: none; letter-spacing: .2px; }

  .tagline-lettering { position: absolute; left: 1018px; top: 106px; width: 142px; height: 104px; background: radial-gradient(ellipse at center, rgba(255,255,255,.16) 0%, rgba(255,255,255,0) 70%); }
  .tagline-arrow { position: absolute; left: 1140px; top: 66px; }

  .brand { position: absolute; left: 150px; top: 160px; display: flex; align-items: center; gap: 12px; }
  .brand-dot { width: 30px; height: 30px; border-radius: 50%; background: var(--accent); }
  .brand-name { color: var(--white); font-size: 58px; font-weight: 700; letter-spacing: -1px; line-height: 1; }

  .hero-copy { position: absolute; left: 30px; top: 331px; width: 536px; text-align: center; color: var(--white); }
  .hero-title { font-size: 34px; font-weight: 700; letter-spacing: .2px; }
  .hero-lead { margin-top: 16px; font-size: 22px; font-weight: 300; line-height: 30px; }
  .hero-lead b { font-weight: 400; }
  .hero-lead strong { font-weight: 700; }
  .cta { position: absolute; left: 216px; top: 527px; width: 165px; height: 58px; background: var(--white); border-radius: 4px; color: #3b3b3b; font-size: 12px; font-weight: 700; letter-spacing: .5px; display: flex; align-items: center; justify-content: center; text-decoration: none; }

  .feed-card { position: absolute; left: 646px; top: 235px; width: 483px; height: 531px; background: var(--white); border-radius: 3px 3px 0 0; overflow: hidden; }
  .feed-cover { height: 193px; background: linear-gradient(180deg, #3f5a45 0%, #5e8367 45%, #2c4632 100%); }
  .feed-author { position: absolute; left: 18px; top: 169px; width: 66px; height: 66px; border: 2px solid var(--white); background: #8d8d8d; border-radius: 2px; }
  .feed-author-name { position: absolute; left: 94px; top: 199px; font-size: 14px; font-weight: 700; color: var(--ink); }
  .feed-post { position: absolute; left: 18px; top: 244px; width: 456px; font-size: 11.6px; line-height: 20px; color: var(--text); }
  .comment { position: absolute; left: 0; width: 483px; height: 100px; border-top: 1px solid var(--rule); }
  .comment-avatar { position: absolute; left: 20px; top: 19px; width: 50px; height: 50px; border-radius: 2px; }
  .comment-name { position: absolute; left: 80px; top: 16px; font-size: 14px; font-weight: 700; color: var(--ink); }
  .comment-date { position: absolute; right: 21px; top: 19px; font-size: 11px; color: var(--accent); }
  .comment-body { position: absolute; left: 80px; top: 45px; width: 395px; font-size: 10.6px; line-height: 20px; color: var(--text); }

  .hero-rule { position: absolute; left: 0; top: 766px; width: 1200px; height: 3px; background: var(--accent); }

  .steps { position: absolute; left: 0; top: 854px; width: 1200px; }
  .step { position: absolute; top: 0; width: 106px; height: 106px; border: 2px solid var(--step-ring); border-radius: 50%; font-size: 40px; font-weight: 300; color: #333; text-align: center; line-height: 100px; }
</style>
</head>
<body>
  <header class="hero">
    <div class="hero-backdrop" role="img" aria-label="Faint illustration of linked social network circles over a dotted world map"></div>

    <nav class="main-nav">
      <a href="#" style="left:643px">PROMOTE IT</a>
      <a href="#" style="left:786px">SHARE TO EARN</a>
      <a href="#" style="left:948px">AFFILIATES</a>
      <a href="#" style="left:1062px">HIREVOICES</a>
    </nav>

    <svg class="tagline-arrow" width="30" height="70" viewBox="0 0 30 70" aria-hidden="true">
      <path d="M6 68 C26 50 26 22 12 6" stroke="#fff" stroke-width="2" fill="none"/>
      <path d="M6 4 L13 4 L12 12" stroke="#fff" stroke-width="2" fill="none"/>
    </svg>
    <div class="tagline-lettering" role="img" aria-label="Hand-lettered note: Hands-On, Ultra-Targeted Campaigns"></div>

    <div class="brand">
      <span class="brand-name">quenvale</span>
      <span class="brand-dot"></span>
    </div>

    <div class="hero-copy">
      <h1 class="hero-title">YOUR CAMPAIGN, SHARED</h1>
      <p class="hero-lead">Get your <b>message</b> moving <b>across social media</b> within minutes <b>Thousands of social voices</b> are on <strong>stand-by and ready to assist</strong></p>
    </div>
    <a class="cta" href="#">LET`S GET STARTED</a>

    <article class="feed-card">
      <div class="feed-cover" role="img" aria-label="Photo of hanging glass light bulbs covered in water drops against a green background"></div>
      <div class="feed-author" role="img" aria-label="Profile photo of Tomas Verhald"></div>
      <div class="feed-author-name">Tomas Verhald</div>
      <p class="feed-post">Nemo enim ipsam voluptatem quia voluptas sit aspernatur aut odit aut fugit, sed quia consequuntur magni dolores eos qui ratione voluptatem sequi nesciunt.</p>

      <div class="comment" style="top:309px">
        <div class="comment-avatar" role="img" aria-label="Profile photo of Lina Maretto" style="background:#6d5a66"></div>
        <div class="comment-name">Lina Maretto</div>
        <div class="comment-date">17/09/2010</div>
        <p class="comment-body">Nemo enim ipsam voluptatem quia voluptas sit aspernatur aut odit aut fugit, sed quia consequuntur magni dolores eos qui ratione voluptatem sequi</p>
      </div>
      <div class="comment" style="top:409px">
        <div class="comment-avatar" role="img" aria-label="Illustrated avatar of Owen Barlow" style="background:#b9cfe0"></div>
        <div class="comment-name">Owen Barlow</div>
        <div class="comment-date">17/09/2010</div>
        <p class="comment-body">Nemo enim ipsam voluptatem quia voluptas sit aspernatur aut odit aut fugit, sed quia consequuntur magni dolores eos qui ratione voluptatem sequi</p>
      </div>
    </article>
  </header>
  <div class="hero-rule"></div>

  <section class="steps">
    <div class="step" style="left:138px">1</div>
    <div class="step" style="left:538px">2</div>
    <div class="step" style="left:938px">3</div>
  </section>
</body>
</html>
```